Vell Partners Building Business Cards

We need a business card that reflects our business as "Solar Experts" in San Diego. Browse our website www.vellpartners.example our License needs to be displayed as "CSLB# 4718392" our phone number is (619) 555-0147

Save thousands on your electric bills and increase the value of your home while helping to protect the environment. Our solar installation experts will help you design the system that's right for you, using only the highest quality equipment that will look great and give you ideal performance. Our goal is to make you energy independent, and get your electric bill to 0.

Tobias Wrenfield
(619) 555-0147
tobias@vellpartners.example

Target Market(s)

Home owners in san diego looking for solar

Industry/Entity Type

Solar Energy

Contact Information for Business Card

Tobias Wrenfield
(619) 555-0147
tobias@vellpartners.example

Font styles to use
Other font styles liked:
• Use our logo font

Requirements
Must have
• License needs to be displayed as "CSLB# 4718392" our phone number is (619) 555-0147
Nice to have
• Real images of rooftop home solar in san diego
Should not have
• our business address

```html
<!DOCTYPE html>
<html lang="en">
<head>
<meta charset="utf-8">
<title>Vell Partners Building – Business Cards</title>
<link rel="stylesheet" href="https://fonts.googleapis.com/css2?family=Open+Sans:wght@400;600;700;800&display=swap">
<style>
  :root {
    --navy: #1f3f82;
    --navy-deep: #16306a;
    --navy-light: #2c55a3;
    --gold: #f6a91c;
    --paper: #ffffff;
    --stage: #e9e9ec;
    --ink-light: #ffffff;
  }
  * { box-sizing: border-box; margin: 0; padding: 0; }
  html, body {
    width: 1200px; height: 950px; overflow: hidden;
    background: var(--stage);
    font-family: "Open Sans", Arial, sans-serif;
  }
  .sheet {
    width: 1200px; height: 950px;
    display: flex; flex-direction: column; align-items: center; justify-content: center;
    gap: 60px;
  }
  .card {
    position: relative; width: 700px; height: 400px; overflow: hidden;
    box-shadow: 0 6px 18px rgba(0,0,0,.18);
  }
  /* front */
  .card--front { background: var(--paper); }
  .card__band { position: absolute; inset: 0; width: 700px; height: 400px; }
  .brand {
    position: absolute; left: 0; right: 0; top: 70px;
    display: flex; align-items: center; justify-content: center; gap: 16px;
  }
  .brand__dot { width: 34px; height: 34px; border-radius: 50%; background: var(--gold); }
  .brand__name {
    font-weight: 800; font-size: 44px; color: var(--navy); letter-spacing: -0.5px;
  }
  .person {
    position: absolute; left: 48px; top: 272px; color: var(--ink-light);
  }
  .person__name { font-weight: 700; font-size: 26px; color: var(--gold); line-height: 1.2; }
  .person__role, .person__license { font-size: 18px; line-height: 1.4; }
  .contact {
    position: absolute; right: 40px; top: 262px;
    list-style: none; color: var(--ink-light); font-size: 18px; line-height: 1.6;
  }
  .contact__item { display: flex; align-items: center; justify-content: flex-end; gap: 12px; }
  .contact__icon { width: 20px; height: 20px; flex: none; }
  /* back */
  .card--back {
    background: linear-gradient(135deg, var(--navy-light) 0%, var(--navy) 45%, var(--navy-deep) 100%);
  }
  .back-mark {
    position: absolute; right: 48px; bottom: 48px;
    display: flex; flex-direction: column; align-items: flex-end; gap: 10px;
  }
  .back-mark__row { display: flex; align-items: center; gap: 14px; }
  .back-mark__dot { width: 44px; height: 44px; border-radius: 50%; background: var(--gold); }
  .back-mark__name { font-weight: 800; font-size: 26px; color: var(--ink-light); }
  .back-mark__web { font-size: 17px; color: var(--ink-light); }
</style>
</head>
<body>
<main class="sheet">
  <section class="card card--front" aria-label="Business card front">
    <svg class="card__band" viewBox="0 0 700 400" aria-hidden="true">
      <defs>
        <linearGradient id="bandFill" x1="0" y1="0" x2="1" y2="0">
          <stop offset="0" stop-color="#2c55a3"/>
          <stop offset="0.5" stop-color="#1f3f82"/>
          <stop offset="1" stop-color="#1c3a7a"/>
        </linearGradient>
      </defs>
      <path d="M0 236 H30 L52 214 H268 L290 236 H700 V400 H0 Z" fill="url(#bandFill)"/>
      <path d="M0 232 H28 L50 210 H270 L292 232 H700" fill="none" stroke="var(--gold)" stroke-width="4"/>
    </svg>

    <div class="brand">
      <span class="brand__dot"></span>
      <span class="brand__name">Vell Partners Building</span>
    </div>

    <div class="person">
      <p class="person__name">Tobias Wrenfield</p>
      <p class="person__role">CEO/Founder</p>
      <p class="person__license">CSLB# 4718392</p>
    </div>

    <ul class="contact">
      <li class="contact__item">(619) 555-0147
        <svg class="contact__icon" viewBox="0 0 20 20" aria-hidden="true"><circle cx="10" cy="10" r="10" fill="var(--gold)"/><path d="M6.5 5h2l1 2.6-1.3 1a6 6 0 0 0 2.9 2.9l1-1.3 2.6 1v2a1 1 0 0 1-1 1A9 9 0 0 1 5.5 6a1 1 0 0 1 1-1z" fill="#1f3f82"/></svg>
      </li>
      <li class="contact__item">tobias@vellpartners.example
        <svg class="contact__icon" viewBox="0 0 20 20" aria-hidden="true"><circle cx="10" cy="10" r="10" fill="var(--gold)"/><rect x="5" y="6.5" width="10" height="7" rx="1" fill="#1f3f82"/><path d="M5.5 7l4.5 3.5L14.5 7" fill="none" stroke="var(--gold)" stroke-width="1"/></svg>
      </li>
      <li class="contact__item">www.vellpartners.example
        <svg class="contact__icon" viewBox="0 0 20 20" aria-hidden="true"><circle cx="10" cy="10" r="10" fill="var(--gold)"/><circle cx="10" cy="10" r="5" fill="none" stroke="#1f3f82" stroke-width="1.3"/><path d="M5 10h10M10 5c-2 3-2 7 0 10M10 5c2 3 2 7 0 10" fill="none" stroke="#1f3f82" stroke-width="1.1"/></svg>
      </li>
    </ul>
  </section>

  <section class="card card--back" aria-label="Business card back">
    <div class="back-mark">
      <div class="back-mark__row">
        <span class="back-mark__name">Vell Partners Building</span>
        <span class="back-mark__dot"></span>
      </div>
      <p class="back-mark__web">www.vellpartners.example</p>
    </div>
  </section>
</main>
</body>
</html>
```